Hollow Lantern Distillery

I need a label designed for my small distillery. I’d like it to have a rose, and the name hollow lantern in script writing. I need the graphic to fit a standard gin bottle and I’ll need to be able to edit it depending on alcohol, warning and descriptions. I want it to look elegant and attractive, but slightly daring too. It’s a 700ml oslo bottle
Target Market(s)
Bespoke gin and vodka drinkers
Industry/Entity Type
Beverage
Font styles to use
Script
Other font styles liked:
- Something easy to read
Requirements
Must have
- Room for me to add and remove text depending on the drink
Nice to have
- Hollow lantern in script, slight colour on the rose and black writing

```html
<!DOCTYPE html>
<html lang="en">
<head>
<meta charset="utf-8">
<title>Hollow Lantern Distillery – Label Range</title>
<link rel="stylesheet" href="https://fonts.googleapis.com/css2?family=Pinyon+Script&family=Libre+Baskerville&family=Oswald:wght@500&display=swap">
<style>
  :root {
    --canvas: #f3f3f2;
    --paper: #fbfbfa;
    --ink: #141414;
    --gold-dark: #c49142;
    --gold-light: #ebcd7a;
    --navy-dark: #1f1c6e;
    --navy-light: #47438f;
    --rose-dark: #e0a7b4;
    --rose-light: #ecbcc6;
    --band-text: #f7efe4;
  }
  * { margin: 0; padding: 0; box-sizing: border-box; }
  html, body { width: 1200px; height: 858px; overflow: hidden; background: var(--canvas); }
  .range { position: relative; width: 1200px; height: 858px; }

  .variant { position: absolute; top: 70px; width: 300px; height: 730px; }
  .variant--gin { left: 80px; --accent-a: var(--gold-dark); --accent-b: var(--gold-light); --line: var(--gold-dark); }
  .variant--vodka { left: 450px; --accent-a: var(--navy-dark); --accent-b: var(--navy-light); --line: var(--navy-dark); }
  .variant--rose { left: 820px; --accent-a: var(--rose-dark); --accent-b: var(--rose-light); --line: var(--rose-dark); }

  /* neck strip */
  .neck-tag {
    position: absolute; left: 129px; top: 0; width: 42px; height: 210px;
    background: var(--paper); padding: 4px;
    filter: drop-shadow(0 2px 4px rgba(0,0,0,.15));
  }
  .neck-tag__frame {
    width: 100%; height: 100%;
    border: 2px solid var(--line);
    display: flex; align-items: center; justify-content: center;
  }
  .neck-tag__name {
    transform: rotate(-90deg); white-space: nowrap;
    font-family: "Pinyon Script", cursive; font-size: 22px; color: var(--ink);
  }

  /* main label */
  .label { position: absolute; left: 0; top: 240px; width: 300px; height: 415px; }
  .label__shape { position: absolute; inset: 0; filter: drop-shadow(0 3px 6px rgba(0,0,0,.14)); }
  .label__shape path { fill: var(--paper); }
  .label__name {
    position: absolute; left: 0; right: 0; top: 46px; text-align: center;
    font-family: "Pinyon Script", cursive; font-size: 50px; line-height: 56px; color: var(--ink);
  }
  .label__rose {
    position: absolute; left: 36px; top: 186px; width: 228px; height: 108px; border-radius: 50px;
    background: radial-gradient(ellipse at center, var(--accent-b) 0%, rgba(255,255,255,0) 72%);
    opacity: .55;
  }
  .label__band {
    position: absolute; left: 0; right: 0; top: 312px; height: 36px;
    background: linear-gradient(90deg, var(--accent-a), var(--accent-b));
    display: flex; align-items: center; justify-content: center;
    font-family: "Libre Baskerville", serif; font-size: 17px; letter-spacing: .5px; color: var(--band-text);
  }
  .label__spec {
    position: absolute; left: 0; right: 0; top: 364px; text-align: center;
    font-family: "Oswald", sans-serif; font-weight: 500; font-size: 13px; color: var(--ink);
  }
</style>
</head>
<body>
<main class="range">

  <section class="variant variant--gin">
    <div class="neck-tag"><div class="neck-tag__frame"><span class="neck-tag__name">Hollow Lantern</span></div></div>
    <div class="label">
      <svg class="label__shape" viewBox="0 0 300 415" width="300" height="415" aria-hidden="true">
        <path d="M150 0 L288 28 Q300 31 300 43 L300 368 Q300 380 288 384 L150 415 L12 384 Q0 380 0 368 L0 43 Q0 31 12 28 Z"/>
      </svg>
      <h2 class="label__name">Hollow<br>Lantern</h2>
      <div class="label__rose" role="img" aria-label="Gold line drawing of roses and blossoms"></div>
      <div class="label__band">GIN</div>
      <p class="label__spec">40% ABV &nbsp;|&nbsp; 700 ML</p>
    </div>
  </section>

  <section class="variant variant--vodka">
    <div class="neck-tag"><div class="neck-tag__frame"><span class="neck-tag__name">Hollow Lantern</span></div></div>
    <div class="label">
      <svg class="label__shape" viewBox="0 0 300 415" width="300" height="415" aria-hidden="true">
        <path d="M150 0 L288 28 Q300 31 300 43 L300 368 Q300 380 288 384 L150 415 L12 384 Q0 380 0 368 L0 43 Q0 31 12 28 Z"/>
      </svg>
      <h2 class="label__name">Hollow<br>Lantern</h2>
      <div class="label__rose" role="img" aria-label="Navy line drawing of roses and blossoms"></div>
      <div class="label__band">VODKA</div>
      <p class="label__spec">40% ABV &nbsp;|&nbsp; 700 ML</p>
    </div>
  </section>

  <section class="variant variant--rose">
    <div class="neck-tag"><div class="neck-tag__frame"><span class="neck-tag__name">Hollow Lantern</span></div></div>
    <div class="label">
      <svg class="label__shape" viewBox="0 0 300 415" width="300" height="415" aria-hidden="true">
        <path d="M150 0 L288 28 Q300 31 300 43 L300 368 Q300 380 288 384 L150 415 L12 384 Q0 380 0 368 L0 43 Q0 31 12 28 Z"/>
      </svg>
      <h2 class="label__name">Hollow<br>Lantern</h2>
      <div class="label__rose" role="img" aria-label="Pink line drawing of roses and blossoms"></div>
      <div class="label__band">ROSE GIN</div>
      <p class="label__spec">40% ABV &nbsp;|&nbsp; 700 ML</p>
    </div>
  </section>

</main>
</body>
</html>
```